Psychotherapy and emotion coaching with feloQuin requires web design

I need a web design for emotion coaching (release of emotional blockages) (psychotherapy) with the target group trauma-related disorders and anxiety disorders. The website should be clear and well-organized, i.e. rather simple. The colors should be light, blue, green and yellow are desirable. The design should radiate security.

A logo already exists and should be used appropriately.

Three columns should describe the following
-Emotion regulation
-Imaginative structure constellations
-Ego-State-Therapy

An outdated draft can be seen here:
www.klarer-mutweg.example
The website should advertise coded in Wordpress.

I need the landing page, for which there are drafts now, and at least one more page (maybe a template) for further information (like "About me")

Target Market(s)

Clients for coaching and therapy with trauma or axienty disorders;

Coding

Coded - Design and coding required

Number of Pages Required

3 page

Font styles to use
Sans Serif

Colors
0054AA
0677BA
7BADD7
CADEEF
E8F1F8
59FF00
82FF00
B8FF75
E3FFCB
F4FFEA
FFF300
FFF600
FEFA6F
FFFEC7
FFFEE8

Requirements
Nice to have
• Title: "More happiness and satisfaction in life"
Should not have
• "Therapy" should not be listed in the header; Instead "More happiness and satisfaction in life"

```html
<!DOCTYPE html>
<html lang="de">
<head>
<meta charset="utf-8">
<title>feloQuin – Mehr Glück und Zufriedenheit im Leben</title>
<link rel="stylesheet" href="https://fonts.googleapis.com/css2?family=Montserrat:ital,wght@0,400;0,500;0,600;0,700;1,400&family=Playfair+Display:wght@700&display=swap">
<style>
:root{
  --blue:#0054AA;
  --blue-mid:#0677BA;
  --blue-soft:#7BADD7;
  --blue-pale:#CADEEF;
  --blue-tint:#E8F1F8;
  --cta-blue:#1B5BA6;
  --ink:#1d1d1f;
  --text:#555a60;
  --dark:#1b1b1b;
  --white:#ffffff;
  --line:#d9dde2;
}
*{box-sizing:border-box;margin:0;padding:0}
html,body{width:1200px;height:4323px;overflow:hidden}
body{font-family:"Montserrat",sans-serif;color:var(--text);background:var(--white);position:relative}
.section{position:absolute;left:0;width:1200px}
.abs{position:absolute}
.serif{font-family:"Playfair Display",serif;font-weight:700;letter-spacing:1px}
.btn{position:absolute;display:flex;align-items:center;justify-content:center;background:var(--blue);color:var(--white);font-size:13px;font-weight:600;border-radius:3px}
.eyebrow{font-size:13px;font-weight:500;color:var(--blue)}
.body-text{font-size:13px;line-height:23px;text-align:justify}
.ticks{list-style:none}
.ticks li{position:relative;padding-left:23px;font-size:13px;line-height:23px;text-align:justify}
.ticks li svg{position:absolute;left:0;top:5px}

/* hero */
.hero{top:0;height:634px;background:linear-gradient(180deg,#6e7d99 0%,#a9a6b4 22%,#8a8ea8 38%,#3d4b6e 50%,#2f4a7e 62%,#3d62a0 80%,#24427a 100%)}
.brand{left:141px;top:22px;display:flex;align-items:center;gap:12px}
.brand-dot{width:46px;height:46px;border-radius:50%;background:#f2c94c}
.brand-name{font-size:18px;font-weight:500;color:var(--white)}
.hero-title{left:0;width:1200px;top:216px;text-align:center;color:var(--white);font-size:50px;line-height:65px}

/* about */
.about{top:634px;height:700px;background:var(--white)}
.person-name{font-size:37px;color:var(--ink)}

/* services slider */
.services{top:1334px;height:784px;background:var(--blue-tint)}
.center-head{left:0;width:1200px;text-align:center}
.h-section{font-size:36px;color:var(--ink)}
.photo{position:absolute;border-radius:14px}
.service-card{left:604px;top:181px;width:420px;height:386px;background:var(--white);border-radius:16px;box-shadow:0 10px 30px rgba(0,40,90,.12);padding:40px 40px}
.service-card h3{font-size:25px;font-weight:500;line-height:35px;color:var(--ink);margin-bottom:18px}
.service-card p{font-size:12.5px;line-height:23px}
.link{font-size:13px;font-weight:500;color:var(--blue);text-decoration:underline}
.round-arrow{position:absolute;width:30px;height:30px;border-radius:50%;display:flex;align-items:center;justify-content:center}

/* anxiety */
.anxiety{top:2118px;height:689px;background:var(--dark)}
.anxiety .h-dark{font-size:36px;line-height:49px;color:var(--white)}
.anxiety .body-text,.anxiety .ticks li{color:#e6e6e6}

/* testimonials */
.testimonials{top:2807px;height:542px;background:var(--white)}
.quote-card{position:absolute;top:197px;width:389px;height:221px;background:var(--white);box-shadow:0 6px 22px rgba(0,0,0,.09);padding:62px 30px 0 30px}
.quote-card p{font-size:12.5px;line-height:23px;font-style:italic;position:relative}
.quote-card .who{font-size:16px;font-weight:600;color:var(--ink);margin-top:20px}
.quote-card .role{font-size:12px;font-weight:500;color:var(--blue);margin-top:6px}
.quote-mark{position:absolute;right:22px;top:18px;font-family:"Playfair Display",serif;font-size:150px;line-height:1;color:#eef1f5}

/* call to action */
.cta{top:3349px;height:463px;background:var(--cta-blue);overflow:hidden}
.cta .h-light{font-size:36px;line-height:49px;color:var(--white)}
.cta .body-text{color:#eaf1fa}

/* contact */
.contact{top:3812px;height:467px;background:var(--white)}
.info-row{position:absolute;left:141px;display:flex;gap:14px;align-items:flex-start}
.info-label{font-size:13px;font-weight:600;color:var(--blue)}
.info-value{font-size:13px;line-height:20px;color:var(--text)}
.field{position:absolute;left:644px;width:415px;border:1px solid var(--line);display:flex;align-items:flex-start;gap:10px;padding:0 14px;font-size:12px;color:#666}
.footer{top:4279px;height:44px;background:var(--blue);color:var(--white);font-size:12px;display:flex;align-items:center;justify-content:center}
</style>
</head>
<body>

<!-- HERO -->
<header class="section hero" role="img" aria-label="Foto: ruhiger See in der Abenddämmerung mit Bergsilhouetten">
  <div class="abs brand">
    <span class="brand-dot"></span>
    <span class="brand-name">feloQuin</span>
  </div>
  <div class="btn" style="left:910px;top:27px;width:149px;height:38px">Kontaktiere Uns</div>
  <h1 class="abs hero-title serif">Mehr Glück Und<br>Zufriedenheit Im Leben</h1>
  <div class="btn" style="left:455px;top:366px;width:290px;height:37px">Kostenloses Erstgespräch Vereinbaren</div>
</header>

<!-- ABOUT -->
<section class="section about">
  <svg class="abs" style="left:134px;top:99px" width="440" height="517" viewBox="0 0 440 517" role="img" aria-label="Porträtfoto des Beraters">
    <defs>
      <linearGradient id="portrait" x1="0" y1="0" x2="0" y2="1">
        <stop offset="0" stop-color="#f4f4f4"/>
        <stop offset=".55" stop-color="#dcd6d3"/>
        <stop offset="1" stop-color="#3f6fc6"/>
      </linearGradient>
    </defs>
    <polyline points="220,516 0,390 0,130" fill="none" stroke="var(--blue)" stroke-width="6"/>
    <polygon points="8,127 220,3 440,127 440,387 220,510 8,387" fill="url(#portrait)"/>
  </svg>
  <div class="abs eyebrow" style="left:644px;top:106px">Über Mich</div>
  <h2 class="abs person-name serif" style="left:644px;top:126px">Jonas Falkner</h2>
  <p class="abs body-text" style="left:644px;top:185px;width:415px">Wenn Sie gerade beispielweise an einem der folgenden Punkte im Leben angekommen sind, unterstütze ich Sie gerne darin, Wege aus der Krise zu finden und Änderungen herbeizuführen:</p>
  <ul class="abs ticks" style="left:644px;top:270px;width:415px">
    <li style="margin-bottom:6px"><svg width="14" height="14" viewBox="0 0 14 14"><circle cx="7" cy="7" r="7" fill="var(--blue)"/><path d="M4 7.2l2 2 4-4.2" stroke="#fff" stroke-width="1.6" fill="none"/></svg>Sie haben oder eine Ihnen nahestehende Person hat eine Diagnose zu einer schwerwiegenden Krankheit, wie Krebs bekommen (Psychoonkologie)</li>
    <li style="margin-bottom:6px"><svg width="14" height="14" viewBox="0 0 14 14"><circle cx="7" cy="7" r="7" fill="var(--blue)"/><path d="M4 7.2l2 2 4-4.2" stroke="#fff" stroke-width="1.6" fill="none"/></svg>Sie leiden unter Ängsten, Phobien oder Krankheiten, wie Tinnitus</li>
    <li style="margin-bottom:6px"><svg width="14" height="14" viewBox="0 0 14 14"><circle cx="7" cy="7" r="7" fill="var(--blue)"/><path d="M4 7.2l2 2 4-4.2" stroke="#fff" stroke-width="1.6" fill="none"/></svg>Sie haben schlimme bzw. traumatische Erfahrungen gemacht und/oder leiden an deren Folgen bzw. an einer posttraumatischen Belastungsstörung</li>
    <li style="margin-bottom:6px"><svg width="14" height="14" viewBox="0 0 14 14"><circle cx="7" cy="7" r="7" fill="var(--blue)"/><path d="M4 7.2l2 2 4-4.2" stroke="#fff" stroke-width="1.6" fill="none"/></svg>Sie haben Schwierigkeiten im Beruf oder mit Ihrem Partner / Ihrer PartnerIn.</li>
    <li><svg width="14" height="14" viewBox="0 0 14 14"><circle cx="7" cy="7" r="7" fill="var(--blue)"/><path d="M4 7.2l2 2 4-4.2" stroke="#fff" stroke-width="1.6" fill="none"/></svg>Sie befinden sich in einer Krise oder Umbruchsituation</li>
  </ul>
  <div class="btn" style="left:644px;top:569px;width:128px;height:39px">Mehr wissen</div>
</section>

<!-- SERVICES SLIDER -->
<section class="section services">
  <div class="abs center-head eyebrow" style="top:83px">Was Wir Tun</div>
  <h2 class="abs center-head h-section serif" style="top:112px">Unsere Dienstleistungen</h2>
  <div class="photo" style="left:0;top:292px;width:141px;height:164px;border-radius:0 14px 14px 0;background:linear-gradient(135deg,#d9dde4,#a8b0be)" role="img" aria-label="Foto: Person hält ein Blatt vor das Gesicht"></div>
  <div class="round-arrow" style="left:82px;top:359px;background:var(--blue-pale)"><svg width="12" height="12" viewBox="0 0 12 12"><path d="M10 6H2M5 3L2 6l3 3" stroke="var(--blue)" stroke-width="1.5" fill="none"/></svg></div>
  <div class="photo" style="left:176px;top:218px;width:428px;height:312px;border-radius:14px 0 0 14px;background:linear-gradient(180deg,#7e9ab8 0%,#5d7d5a 45%,#d8cbb2 100%)" role="img" aria-label="Foto: Mann steht mit ausgebreiteten Armen am Strand"></div>
  <div class="abs" style="left:600px;top:218px;width:6px;height:312px;background:var(--blue)"></div>
  <div class="abs service-card">
    <h3>Systemische Strukturaufstellungen</h3>
    <p>Wir alle haben überkommene Prägungen und Muster, die immer wieder Konfliktverursachen oder uns ausbremsen. In einer Aufstellung werden alte Muster aufgedeckt und verändert, sodass du an Klarheit undSelbstakzeptanzgewinnst und es dir mehr und mehr gelingt, eine glückliche Partnerschaft zu führen oder sich Konflikte im Team lösen.</p>
    <div class="link" style="margin-top:18px">Kontaktiere Uns</div>
  </div>
  <div class="photo" style="left:1059px;top:292px;width:141px;height:164px;border-radius:14px 0 0 14px;background:linear-gradient(135deg,#cfd8e2,#7d8a99)" role="img" aria-label="Foto: zwei Personen im Gespräch"></div>
  <div class="round-arrow" style="left:1087px;top:359px;background:var(--blue)"><svg width="12" height="12" viewBox="0 0 12 12"><path d="M2 6h8M7 3l3 3-3 3" stroke="#fff" stroke-width="1.5" fill="none"/></svg></div>
  <p class="abs" style="left:0;width:1200px;top:592px;text-align:center;font-size:13px;line-height:23px;color:#333">Die Methoden eignen sichfür Coaching und Therapie gleichermaßen. Kontaktiere mich gerne,<br>wenn du z.B. an Depression, Angststörungen, Süchten oder Zwängen leidest.</p>
  <div class="btn" style="left:525px;top:661px;width:148px;height:39px">Kontaktiere Uns</div>
</section>

<!-- ANXIETY -->
<section class="section anxiety">
  <h2 class="abs h-dark serif" style="left:141px;top:78px;width:500px">Leidest Du Unter Angstzuständen, Traumata Oder Emotionalen Belastungen?</h2>
  <p class="abs body-text" style="left:141px;top:285px;width:415px">Unser Gehirn merkt sich Erfahrungen, die schwerwiegend waren oder uns in einer traumatischen Situation überfordert haben. Wenn wir unbewusst an solche Erfahrungen erinnert werden, sind wir nicht mehr voll und ganz handlungsfähig und fühlen uns schlecht</p>
  <div class="abs" style="left:141px;top:413px;font-size:14px;font-weight:600;color:var(--white)">Vorteile</div>
  <ul class="abs ticks" style="left:141px;top:453px;width:415px">
    <li style="margin-bottom:9px"><svg width="14" height="14" viewBox="0 0 14 14"><circle cx="7" cy="7" r="7" fill="var(--blue-mid)"/><path d="M4 7.2l2 2 4-4.2" stroke="#fff" stroke-width="1.6" fill="none"/></svg>Verbesserte Emotionsregulierung</li>
    <li style="margin-bottom:9px"><svg width="14" height="14" viewBox="0 0 14 14"><circle cx="7" cy="7" r="7" fill="var(--blue-mid)"/><path d="M4 7.2l2 2 4-4.2" stroke="#fff" stroke-width="1.6" fill="none"/></svg>Geringere Ängste</li>
    <li><svg width="14" height="14" viewBox="0 0 14 14"><circle cx="7" cy="7" r="7" fill="var(--blue-mid)"/><path d="M4 7.2l2 2 4-4.2" stroke="#fff" stroke-width="1.6" fill="none"/></svg>Größeres Selbstbewusstsein</li>
  </ul>
  <div class="btn" style="left:141px;top:567px;width:319px;height:37px">Kostenloses Erstgespräch Vereinbaren</div>
  <svg class="abs" style="left:612px;top:94px" width="450" height="530" viewBox="0 0 450 530" role="img" aria-label="Illustration: Kopf im Profil mit sichtbarem, mechanischem Gehirn">
    <defs>
      <linearGradient id="brain" x1="0" y1="0" x2="1" y2="1">
        <stop offset="0" stop-color="#e9dfcd"/>
        <stop offset=".5" stop-color="#9a6e5a"/>
        <stop offset="1" stop-color="#4f6a8f"/>
      </linearGradient>
    </defs>
    <polyline points="5,395 5,130 225,5" fill="none" stroke="var(--blue)" stroke-width="6"/>
    <polygon points="12,133 225,12 442,133 442,397 225,520 12,397" fill="url(#brain)"/>
  </svg>
</section>

<!-- TESTIMONIALS -->
<section class="section testimonials">
  <div class="abs center-head eyebrow" style="top:83px">Was Wir Tun</div>
  <h2 class="abs center-head h-section serif" style="top:116px">Unsere Dienstleistungen</h2>

  <div class="round-arrow" style="left:82px;top:281px;background:var(--blue-pale)"><svg width="12" height="12" viewBox="0 0 12 12"><path d="M10 6H2M5 3L2 6l3 3" stroke="var(--blue)" stroke-width="1.5" fill="none"/></svg></div>
  <div class="round-arrow" style="left:1087px;top:281px;background:var(--blue)"><svg width="12" height="12" viewBox="0 0 12 12"><path d="M2 6h8M7 3l3 3-3 3" stroke="#fff" stroke-width="1.5" fill="none"/></svg></div>

  <article class="quote-card" style="left:185px">
    <span class="quote-mark">”</span>
    <p>“Lorem Ipsum is simply dummy text of the printing and typesetting industry. Lorem Ipsum has been the industry's standard dummy text ever since the 1500s, when an unknown printer took .”</p>
    <div class="who">Lorem Ipsum</div>
    <div class="role">Lorem Ipsum</div>
  </article>
  <article class="quote-card" style="left:626px">
    <span class="quote-mark">”</span>
    <p>“Lorem Ipsum is simply dummy text of the printing and typesetting industry. Lorem Ipsum has been the industry's standard dummy text ever since the 1500s, when an unknown printer took .”</p>
    <div class="who">Lorem Ipsum</div>
    <div class="role">Lorem Ipsum</div>
  </article>
  <svg class="abs" style="left:216px;top:172px" width="46" height="50" viewBox="0 0 46 50"><polygon points="23,0 46,12.5 46,37.5 23,50 0,37.5 0,12.5" fill="var(--blue)"/><path d="M13 21h7v8h-4c0 3 1 4 3 4v3c-4 0-6-3-6-7zM25 21h7v8h-4c0 3 1 4 3 4v3c-4 0-6-3-6-7z" fill="#fff"/></svg>
  <svg class="abs" style="left:657px;top:172px" width="46" height="50" viewBox="0 0 46 50"><polygon points="23,0 46,12.5 46,37.5 23,50 0,37.5 0,12.5" fill="var(--blue)"/><path d="M13 21h7v8h-4c0 3 1 4 3 4v3c-4 0-6-3-6-7zM25 21h7v8h-4c0 3 1 4 3 4v3c-4 0-6-3-6-7z" fill="#fff"/></svg>

  <div class="abs" style="left:577px;top:456px;display:flex;gap:4px;align-items:center">
    <span style="width:8px;height:2px;background:var(--blue-pale)"></span>
    <span style="width:16px;height:3px;background:var(--blue)"></span>
    <span style="width:8px;height:2px;background:var(--blue-pale)"></span>
  </div>
</section>

<!-- CALL TO ACTION -->
<section class="section cta">
  <svg class="abs" style="left:0;top:0" width="1200" height="463" viewBox="0 0 1200 463">
    <defs>
      <linearGradient id="ctaPhoto" x1="0" y1="0" x2="0" y2="1">
        <stop offset="0" stop-color="#efe3da"/>
        <stop offset="1" stop-color="#d9cfc8"/>
      </linearGradient>
    </defs>
    <line x1="690" y1="0" x2="900" y2="463" stroke="#3f78bf" stroke-width="1"/>
    <line x1="1120" y1="260" x2="1200" y2="360" stroke="#3f78bf" stroke-width="1"/>
    <polygon points="100,330 300,400 300,463 100,400" fill="#ffffff"/>
    <polygon points="360,400 560,330 560,400 360,463" fill="#ffffff"/>
    <polygon points="150,60 330,-10 510,60 510,330 330,430 150,330" fill="url(#ctaPhoto)" role="img" aria-label="Foto: lächelnde Frau mit Laptop"/>
  </svg>
  <h2 class="abs h-light serif" style="left:644px;top:56px;width:420px">Bereit, Den Ersten Schritt Zu Gehen?</h2>
  <p class="abs body-text" style="left:644px;top:157px;width:415px">Gerne können wir einen Termin für ein Erstgespräch vereinbaren, dass auf Wunsch auch telefonisch stattfinden kann. In dem Erstgespräch stehen ein erstes Kennenlernen, sowie Ihre Ziele und Erwartungen im Vordergrund. Im weiteren Verlauf entscheiden beide, ob eine Zusammenarbeit erfolgen soll, sodass dann die Vorgehensweise sowie die weiteren Termin geplant werden können.</p>
  <p class="abs" style="left:644px;top:326px;font-size:13px;color:#eaf1fa">Das ca. 45 minütige Erstgespräch ist kostenlos.</p>
  <div class="btn" style="left:644px;top:371px;width:289px;height:39px;background:var(--white);color:var(--blue)">Kostenloses Erstgespräch Vereinbaren</div>
</section>

<!-- CONTACT -->
<section class="section contact">
  <div class="abs eyebrow" style="left:141px;top:85px">In Kontakt Kommen</div>
  <h2 class="abs serif" style="left:141px;top:110px;font-size:36px;color:var(--ink)">Ihr Berater Jonas</h2>
  <p class="abs body-text" style="left:141px;top:162px;width:415px">Wenn Sie Interesse an meinem Angebot oder Fragen dazu haben, rufen Sie mich gerne an oder schreiben mir eine E-Mail.</p>

  <div class="info-row" style="top:230px">
    <svg width="44" height="48" viewBox="0 0 44 48"><polygon points="22,0 44,12 44,36 22,48 0,36 0,12" fill="var(--blue)"/><path d="M22 15a6 6 0 0 0-6 6c0 5 6 11 6 11s6-6 6-11a6 6 0 0 0-6-6zm0 8.3a2.3 2.3 0 1 1 0-4.6 2.3 2.3 0 0 1 0 4.6z" fill="#fff"/></svg>
    <div><div class="info-label">ADDRESS:</div><div class="info-value">Lindenweg 42, 38100<br>Musterstadt</div></div>
  </div>
  <div class="info-row" style="top:304px">
    <svg width="44" height="48" viewBox="0 0 44 48"><polygon points="22,0 44,12 44,36 22,48 0,36 0,12" fill="var(--blue)"/><path d="M17 16l3 0 2 5-2 1.5c1 2 2.5 3.5 4.5 4.5L26 25l5 2v3c0 1-1 2-2 2-7 0-13-6-13-13 0-1 .5-3 1-3z" fill="#fff"/></svg>
    <div><div class="info-label">CALL US:</div><div style="font-size:20px;font-weight:600;color:var(--ink);line-height:26px">0151 000 00 000</div></div>
  </div>
  <div class="info-row" style="top:378px">
    <svg width="44" height="48" viewBox="0 0 44 48"><polygon points="22,0 44,12 44,36 22,48 0,36 0,12" fill="var(--blue)"/><rect x="13" y="17" width="18" height="13" rx="1.5" fill="#fff"/><path d="M13.5 18l8.5 6.5 8.5-6.5" stroke="var(--blue)" stroke-width="1.4" fill="none"/></svg>
    <div><div class="info-label">EMAIL:</div><div class="info-value">kontakt@feloquin.example</div></div>
  </div>

  <div class="field" style="top:104px;height:34px;align-items:center">
    <svg width="11" height="11" viewBox="0 0 12 12"><circle cx="6" cy="3.5" r="3" fill="var(--blue)"/><path d="M0 12c0-3.5 2.7-5 6-5s6 1.5 6 5z" fill="var(--blue)"/></svg>Name
  </div>
  <div class="field" style="top:158px;height:34px;align-items:center">
    <svg width="11" height="11" viewBox="0 0 12 12"><path d="M1.5 1h3l1 3-1.5 1c.8 1.6 2 2.8 3.5 3.5L8.5 7l3 1v3c0 .6-.5 1-1 1C5 12 0 7 0 1.5 0 1 .5 1 1.5 1z" fill="var(--blue)"/></svg>Phone
  </div>
  <div class="field" style="top:212px;height:34px;align-items:center">
    <svg width="12" height="10" viewBox="0 0 12 10"><rect width="12" height="10" rx="1" fill="var(--blue)"/><path d="M.5 1l5.5 4 5.5-4" stroke="#fff" stroke-width="1" fill="none"/></svg>Email
  </div>
  <div class="field" style="top:265px;height:68px;padding-top:10px">
    <svg width="12" height="12" viewBox="0 0 12 12"><rect x="0.5" y="1.5" width="9" height="9.5" fill="none" stroke="var(--blue)"/><path d="M5 7l6-6" stroke="var(--blue)" stroke-width="1.5"/></svg>Message
  </div>
  <div class="abs" style="left:672px;top:380px;font-size:13px;font-weight:600;color:var(--blue)">Einreichen</div>
</section>

<footer class="section footer">©2024 feloQuin Coaching. All Rights Reserved.</footer>

</body>
</html>
```